Spa Brochure/service menu for existing spa for men and women

We need a brochure redesign to match our new logo, and business cards. Please keep in mind we love simplicity and no orchids. Tri-fold. unique. simple. eye catching front. Brochure serves as service menu in and out of business. Our clientel base is equal parts men and women. We are a privately owned and very unique business and would like our brochure to reflect that.

Target Market(s)

Men and women between 30- 65 from the greater NY area on a getaway in our quaint town

Industry/Entity Type

Business

Other font styles liked:
• Avalon. Anything that compliments current fonts in print and logo

Requirements
Must have
• Black, White and Gold design sticking with our new business cards (see attachement). Straight forward and clean. Our biggest concern is the front page being clean and appealing. (open to ideas) Logo on front page as main focus, design in background to highlight it a plus.
Nice to have
• Unique design. A simple map of our location in relation to Main Street and the ski slope on back page. Snail design featured.
Should not have
• No orchids. We hate orchids. No overly feminine tones. No generic spa images etc.

```html
<!DOCTYPE html>
<html lang="en">
<head>
<meta charset="utf-8">
<title>Spa Service Menu</title>
<link href="https://fonts.googleapis.com/css2?family=Questrial&display=swap" rel="stylesheet">
<style>
  :root {
    --ink: #0b0b0b;
    --gold: #c9aa6c;
    --band: #c4a86f;
    --text: #f1f1f1;
    --rule: #3d3d3d;
  }
  html, body { margin: 0; padding: 0; overflow: hidden; background: var(--ink); }
  .menu {
    position: relative; width: 1200px; height: 848px; overflow: hidden;
    background: var(--ink); font-family: "Questrial", sans-serif; color: var(--text);
  }
  .band { position: absolute; left: 0; width: 100%; height: 9px; background: var(--band); }
  .band--top { top: 0; }
  .band--bottom { bottom: 0; }
  .divider { position: absolute; top: 9px; bottom: 9px; width: 1px; background: var(--rule); }
  .guide { position: absolute; width: 1px; background: var(--gold); }
  .guide::before {
    content: ""; position: absolute; top: -4px; left: -4px;
    width: 9px; height: 9px; border-radius: 50%; background: var(--gold);
  }
  .section-title {
    position: absolute; margin: 0; font-weight: 400; font-size: 47px; line-height: 1;
    color: var(--text); writing-mode: vertical-rl; transform: rotate(180deg); white-space: nowrap;
  }
  .service { position: absolute; width: 300px; }
  .service h3 {
    margin: 0; font-weight: 400; font-size: 19px; line-height: 22px; color: var(--gold);
    position: relative; white-space: nowrap;
  }
  .service h3::before {
    content: "•"; position: absolute; left: -10px; color: var(--text); font-size: 13px;
  }
  .service h3 small { font-size: 15px; }
  .service p { margin: 4px 0 0; font-size: 13px; line-height: 16px; }
  .tagline {
    position: absolute; margin: 0; font-weight: 400; font-size: 64px; line-height: 1;
    color: var(--gold); white-space: nowrap;
  }
</style>
</head>
<body>
<main class="menu">
  <div class="band band--top"></div>
  <div class="band band--bottom"></div>
  <div class="divider" style="left:400px"></div>
  <div class="divider" style="left:800px"></div>

  <!-- Massages -->
  <div class="guide" style="left:37px; top:31px; height:478px"></div>
  <h2 class="section-title" style="left:14px; bottom:123px">Massages</h2>

  <section class="service" style="left:81px; top:25px">
    <h3>Swedish</h3>
    <p>Relaxing and therapeutic.<br>Ease tension and enhance circulation.<br>Great for a first time massage or any spa veteran.</p>
  </section>
  <section class="service" style="left:81px; top:134px">
    <h3>Deep Tissue</h3>
    <p>A therapeutic combination of slow and deep pressure alleviates chronic pain, muscle fatigue, and limited range of motion. Muscle Therapy lotion or creme.</p>
  </section>
  <section class="service" style="left:81px; top:247px">
    <h3>Tension Tamer</h3>
    <p>Head, neck and shoulders.<br>Deep Tissue with towels, muscle soothing oils, and cups.</p>
  </section>
  <section class="service" style="left:81px; top:346px">
    <h3>Hot Stone</h3>
    <p>Unforgettable.<br>Warm basalt lava stones melt away all stress and tensions in sore muscles and joints.<br>The ultimate Aprés ski treat.</p>
  </section>
  <section class="service" style="left:81px; top:460px">
    <h3>Recovery</h3>
    <p>Specific to your athletic needs,<br>whether pro or a weekend warrior.<br>Relax, stretch and recover.</p>
  </section>
  <section class="service" style="left:81px; top:556px">
    <h3>Synergy</h3>
    <p>East meets West. Old meets new.<br>A therapeutic blend of cupping, hot stone, Ayurvedic kansa and Italian Marble rolling.</p>
  </section>
  <section class="service" style="left:81px; top:661px">
    <h3>Prenatal</h3>
    <p>Ultimate treat for Mother-to-be.<br>Soothes aches and pains during pregnancy.<br>Mother must be out of 1st trimester.</p>
  </section>
  <p class="tagline" style="left:23px; top:766px">Slow down...</p>

  <!-- Facials -->
  <h2 class="section-title" style="left:411px; top:24px">Facials</h2>
  <div class="guide" style="left:432px; top:184px; height:634px"></div>

  <section class="service" style="left:466px; top:25px; width:320px">
    <h3>Seasonal</h3>
    <p>Call spa concierge for details.</p>
  </section>
  <section class="service" style="left:466px; top:77px; width:320px">
    <h3>Healing Manuka Honey</h3>
    <p>A must for dull, dry or damaged skin.<br>Relieves facial tension, hydrates and plumps.</p>
  </section>
  <section class="service" style="left:466px; top:149px; width:310px">
    <h3>Age-Defying Facial</h3>
    <p>Our organic detox firming peel resurfaces, hydrates and delivers vital nutrients for younger, healthier skin.</p>
  </section>
  <section class="service" style="left:466px; top:235px; width:310px">
    <h3>Arctic Berry illuminating Facial</h3>
    <p>Replenish and restore elasticity. Top of the line Organic peel with minimum reaction and maximum results. All organic.</p>
  </section>
  <section class="service" style="left:466px; top:325px; width:310px">
    <h3>Vitamin C</h3>
    <p>Ideal for all skin types. Potent Vitamin C &amp; E reduces appearance of sun damage, fine lines and wrinkles. Organic and revolutionary stable Vitamin C.</p>
  </section>
  <section class="service" style="left:466px; top:424px; width:300px">
    <h3>Deep Cleansing</h3>
    <p>A deeper clean with clarifying enzymes and vacuum extraction. Won't aggravate sensitive and temperamental skin.</p>
  </section>
  <section class="service" style="left:466px; top:512px; width:320px">
    <h3>Clear Skin</h3>
    <p>Cleanse and clarify problem skin with the power of organic tea tree oil, alpha hydroxy acid and cucumber. Healing probiotics help precent future breakouts and treat blemished, inflamed skin.</p>
  </section>
  <section class="service" style="left:466px; top:614px; width:320px">
    <h3>Microdermabrasion</h3>
    <p>Reduce wrinkles, scarring, discoloration, sun damage, large pores and age spots. Stimulate collagen and elastin production through diamond and crystal exfoliation. Best in series of six. (Immediately reveal younger smoother skin. Dramatically reduce).</p>
  </section>
  <section class="service" style="left:466px; top:749px; width:320px">
    <h3>Calm Skin <small>(Rosacea and Sensitive Skin)</small></h3>
    <p>Soothe and balance the complexion. Reduce irritation and redness with chamomile and arnica, while hydrating and healing.</p>
  </section>

  <!-- Hand & Foot Care -->
  <div class="guide" style="left:838px; top:31px; height:308px"></div>
  <h2 class="section-title" style="left:817px; bottom:123px">Hand &amp; Foot Care</h2>

  <section class="service" style="left:880px; top:25px">
    <h3>Petitie Manicure</h3>
    <p>Snip, clip, file, polish and voile.</p>
  </section>
  <section class="service" style="left:880px; top:93px">
    <h3>Classic Manicure</h3>
    <p>A warm soak, hand and arm massage, nail shaping and cuticle care followed by your choice of enamel.</p>
  </section>
  <section class="service" style="left:880px; top:194px">
    <h3>French Manicure +$5</h3>
  </section>
  <section class="service" style="left:880px; top:244px">
    <h3>Hollow Creek Spa Manicure</h3>
    <p>In addition to a Classic manicure, a gentle exfoliation, soothing masque and hydrating Sedona mud &amp; paraffin dip. Relax, baby soft, beautiful.</p>
  </section>
  <section class="service" style="left:880px; top:364px">
    <h3>Classic Pedicure</h3>
    <p>Green tea foot soak, peppermint exfoliation foot scrub, massage, nail care and polish.</p>
  </section>
  <section class="service" style="left:880px; top:450px">
    <h3>French Pedicure +10</h3>
  </section>
  <section class="service" style="left:880px; top:497px">
    <h3>Hollow Creek Spa Pedicure</h3>
    <p>In addition to a classic pedicure, a soothing anti-inflammatory mud mask and revitalizing foot, calf massage, Sedona mud paraffin treatment. Topped off with your choice of enamel</p>
  </section>
  <section class="service" style="left:880px; top:628px">
    <h3>Apothecary-Pedi</h3>
    <p>Create your one of a kind Pedicure experience. A consultation, creation and service to match a person as unique as you. Bespoke soak, scrub and masque.<br>Includes nail care, massage, and enamel.</p>
  </section>
  <p class="tagline" style="left:852px; top:766px">...Enjoy life</p>
</main>
</body>
</html>
```